Energy Supplement Company Needs Packaging Design! See Your Design In Stores Everywhere!

Have you ever dreamed of seeing your designs on store shelves, billboards and in the hands of celebrities and professional athletes?

Well, your dreams may just come true… You now have the chance to have your design on the product packaging of the next major energy supplement company!

BRISKLO Vigor, Inc. is inviting the most creative, ambitious and talented designers to create a new look and feel for our brand's most popular products, the BRISKLO Vigor Tablets.

BRISKLO Vigor, Inc. began in 1985 by creating the original energy tablet, most recognized for its iconic blue packet featured in over 20,000 retail stores today. The company grew through their grass roots philosophy of distribution and quickly expanded across the United States through dozens of regional and national chains like 4-22, Marlow Q and PVD. In February of 2001, the founder of BriskLo passed and the company’s grass roots approach lost momentum and distribution as the fierce competition from energy shots and drinks hit the space that they once owned.

Theodore Lasko, a 26 year user of BRISKLO tablets, noticed that his favorite daily energy product was becoming increasingly more difficult to find in stores. As an active, serial entrepreneur with numerous ventures, his deep passion for BRISKLO led him to explore the opportunity to get involved with the company (get involved is an understatement). On August 1st of 2012, Theo raised capital and bought the company.

To increase awareness and spread his passion for BRISKLO, Mr. Lasko organized and structured the new BRISKLO Vigor, Inc. by bringing on a talented Team and investors, including Rex Palmore, a renowned sports agent/owner of the largest basketball agency whose clients include some of the biggest names in the sport. The amazing quality of our products coupled with the loyal following from the masses has led the brand to new heights and sponsorship opportunities with major sports teams and athletic organizations.

Now that the future is looking UP, we are looking for a brand refresh to bring our tablets current.

Your mission -should you chose to accept- is to develop a new graphic design for our energy tablet packets. We expect the graphic design to be modern, sleek and appealing to an 18-34 demographic. This new design will serve as the vehicle to spark excitement about energy tablets and their superiority over other forms of energy supplements. However, most importantly, you must make the package eye catching yet trusting and approachable. Keep in mind that this is something you would see in a retail store and feel comfortable reaching for and trying.

It is important to stress the mainstream direction of our company. The current packaging is somewhat 'dated' and may be out of touch with mainstream interests. Just like your aunt still rocking shoulder pads and leg warmers, we need to leave the 1980s and join everyone in 2013. Although we will begin positioning our brand towards mainstream sports, our goal is to have our products everywhere from the sidelines of major sporting events to board meetings of fortune 500 companies to the backpacks of college students. Therefore, the winning design will be one that transcends the interests of a specific group and appeals to the broader audience. Remember this is something you could see Darnell Voss, Otto Frame, and your mother holding.

Here's the great part: We are leaving all of the designing up to you!

You can redesign everything and anything you want (change colors, company logo design, content, etc.). Think of it as a blank canvas.

If you have any questions regarding design or BRISKLO Vigor, Inc. in general, please feel free to email us at design@brisk-lo.example or check out our website at www.brisk-lo.example.

Good luck!

Hi Everyone! 

Thank you to everyone who has submitted designs! Seeing what you all have come up with is exciting and impressive. However, we want to address a few commonly asked questions as well as a few general comments we have overall. 

To start, we'll better explain what we want to see in the designs. 

Although we are an energy company, we are looking to be very contemporary and sleek. Our current brand and packaging is bright and colorful, but that doesn't necessarily fit with the repositioning of our brand as a mainstream energy brand. Designs should try to only include a few colors at most. Each tablet packet should look great one their own and amazing together. 

Moreover, the designs should be relatively minimalistic. We aren't looking for anything to be "in your face". We need to reintroduce to the 18-34 generation that taking energy tablets are safe, effective, and a superior way of consuming energy supplements. Therefore, an approachable packet design is imperative. Neon colors, electricity, etc. only makes the product look scary and intimidating. 

To sum up:
Ø Use only a few colors
Ø Target an 18-34 year old demographic
Ø Minimalistic/approachable design
Ø Move away from Retro look with bright colors

FAQs:
1) We have been asked about whether or not you should be redesigning the logo on the packaging also. The answer is YES. We want every part of the packets updated. You are also designing 3 different packets or our whole energy tablet line (Surge Mix, Summit Mix, and Botanic Mix). 

2) The packets have a height of 4'' and a width of 3''. They are double-sided, so if you have a creative way of designing the back panel with the supplement facts, we would love to see it. 

We want all of you to know that we appreciate all of your hard work on creating these designs and helping to rebrand our company. Again, if you have any questions at all, the best way to reach us is by emailing us at design@brisk-lo.example. 

THANK YOU!!

The BRISKLO Design Team

Reason: We are extending the deadline for designs until Friday April 26th. We hope this will give designers a chance to submit final designs for the competition. As always, please feel free to email us directly at design@brisk-lo.example if you have any questions.

Hi everyone!

Just to let you all know, the design contest ends at 1:37am on Saturday, April 27th. We didn't want to mislead any of you by saying the contest ends tomorrow since you only have an hour and a half to submit any designs after 12am tonight. Therefore, we suggest you submit any designs you want considered by tonight. 

Thanks and good luck! 

The BRISKLO Design Team

Target Market(s)

18-34 year olds. Active, mainstream audience (not extreme-sports fans)

Requirements
Must have
• Product packet is 4''x3''
Should not have
• -Pictures of sports equipment.
-Resemble other energy products
-Look scary or intimidating
-Should not look like a cartoon or animation
-No neon colors

```html
<!DOCTYPE html>
<html lang="en">
<head>
<meta charset="utf-8">
<title>BRISKLO Vigor Botanic Mix Packet</title>
<link rel="stylesheet" href="https://fonts.googleapis.com/css2?family=Oswald:wght@500;600;700&display=swap">
<style>
  :root {
    --backdrop: #e6e6e6;
    --packet-green-dark: #1d9b38;
    --packet-green-light: #2cb24c;
    --ink-white: #ffffff;
  }
  * { margin: 0; padding: 0; box-sizing: border-box; }
  html, body {
    width: 1200px;
    height: 1000px;
    overflow: hidden;
    background: var(--backdrop);
  }
  .canvas {
    position: relative;
    width: 1200px;
    height: 1000px;
    background: var(--backdrop);
    font-family: "Oswald", sans-serif;
    color: var(--ink-white);
  }
  .packet {
    position: absolute;
    left: 380px;
    top: 158px;
    width: 464px;
    height: 646px;
    background: linear-gradient(90deg, var(--packet-green-dark), var(--packet-green-light));
  }
  .packet > * { position: absolute; }
  .blend-name {
    left: 0; right: 0;
    top: 24px;
    text-align: center;
    font-size: 94px;
    font-weight: 700;
    line-height: 1;
    letter-spacing: 1px;
  }
  .blend-contents {
    left: 0; right: 0;
    top: 128px;
    padding-left: 30px;
    text-align: center;
    font-size: 15px;
    font-weight: 600;
    line-height: 1;
  }
  .brand-name {
    left: 0; right: 0;
    top: 200px;
    text-align: center;
    font-size: 86px;
    font-weight: 700;
    line-height: 1;
    letter-spacing: 1px;
  }
  .key-ingredients {
    left: 0; right: 0;
    top: 328px;
    text-align: center;
    font-size: 23px;
    font-weight: 600;
    line-height: 1;
  }
  .product-line {
    left: 0; right: 0;
    top: 368px;
    display: flex;
    justify-content: center;
    align-items: center;
    gap: 14px;
    font-size: 66px;
    font-weight: 700;
    line-height: 1;
  }
  .product-line svg { width: 26px; height: 26px; fill: var(--ink-white); }
  .divider {
    left: 28px;
    top: 494px;
    width: 407px;
    height: 6px;
    background: var(--ink-white);
  }
  .packet-size {
    left: 30px;
    top: 540px;
    line-height: 1;
  }
  .packet-size-label { font-size: 17px; font-weight: 600; }
  .packet-size-value { font-size: 32px; font-weight: 600; margin-top: 8px; }
  .free-from {
    left: 266px;
    top: 527px;
    display: flex;
    gap: 18px;
  }
  .free-from-item {
    width: 44px;
    text-align: center;
    line-height: 1;
  }
  .free-from-badge {
    width: 36px; height: 36px;
    margin: 0 auto;
    border: 3px solid var(--ink-white);
    border-radius: 50%;
    display: flex;
    align-items: center;
    justify-content: center;
    font-size: 20px;
    font-weight: 700;
  }
  .free-from-label { font-size: 11px; font-weight: 600; margin-top: 6px; }
  .supplement-note {
    left: 268px;
    top: 584px;
    font-size: 19px;
    font-weight: 600;
    line-height: 1;
  }
</style>
</head>
<body>
  <main class="canvas">
    <section class="packet">
      <h1 class="blend-name">HERBAL</h1>
      <p class="blend-contents">Minerals, Amino Acids, Enzymes, B-Vitamins, Antioxidants</p>
      <h2 class="brand-name">BRISKLO</h2>
      <p class="key-ingredients">CoQ10*Ginseng*Ginkgo</p>
      <p class="product-line">
        <svg viewBox="0 0 24 24" aria-hidden="true"><polygon points="12,1 15,9 23.5,9 16.5,14 19.2,22.5 12,17.3 4.8,22.5 7.5,14 0.5,9 9,9"/></svg>
        <span>VIGOR</span>
        <svg viewBox="0 0 24 24" aria-hidden="true"><polygon points="12,1 15,9 23.5,9 16.5,14 19.2,22.5 12,17.3 4.8,22.5 7.5,14 0.5,9 9,9"/></svg>
      </p>
      <div class="divider"></div>
      <div class="packet-size">
        <p class="packet-size-label">ProductPacket is</p>
        <p class="packet-size-value">4x3</p>
      </div>
      <div class="free-from">
        <div class="free-from-item"><div class="free-from-badge">0</div><p class="free-from-label">Calories</p></div>
        <div class="free-from-item"><div class="free-from-badge">0</div><p class="free-from-label">Sugar</p></div>
        <div class="free-from-item"><div class="free-from-badge">0</div><p class="free-from-label">Gluten</p></div>
      </div>
      <p class="supplement-note">Dietary Supplement</p>
    </section>
  </main>
</body>
</html>
```